Boost Your Rankings - Search Engine Website

I am launching an SEO website and I am looking to have the site designed. There are a total of 8-10 pages that will need to be designed. I am providing 2 pages off the bat and will work with a designer once these 2 pages are complete. I have never posted a contest for website design (only logos, brochures, etc) so please let me know if there is anything you need from me. I am uploading 2 versions of our logo - a horizontal and a vertical version. I was thinking of getting these rendered in 3d, but I am just going with these for now. I am hoping to complete all work in 10 days, so hopefully the right design for the 1st 2 pages are submitted promptly.

We provide search engine optomization tools and backlinking tools. We provide free research tools as well as cost effective packages for SEO.

I am including 2 word files that have info about the home page and keyword summary page. Additional pages will include: Keyword Research Summary, The Que, Reports, etc.

I am also uploading a zip file that has some examples of home pages that I like. None of them are exactly what I am looking for, but they have certain elements that I like.

I am looking for a clean design and stands out and has good use of color.

Link to instructions files (2...more will be uploaded as first 2 pages are finalized): https://www.filevanta.net/sh/k4m2w7r9x3q5z8/Lp_Tn-7uy2

Forgot to include our logos. Here is a drop box link to the logos: 

https://www.filevanta.net/sh/93jd7fw2mx8qzpa/4Hy_Wq8eTn

big and small businesses, resellers

Seo

• see attached MS Word files for details about requirements.

```html
<!DOCTYPE html>
<html lang="en">
<head>
<meta charset="utf-8">
<title>RankLift.net – Search Engine Rankings</title>
<link href="https://fonts.googleapis.com/css2?family=Roboto+Condensed:wght@300;400;700&family=Open+Sans:ital,wght@0,400;0,700;1,400&display=swap" rel="stylesheet">
<style>
:root{
  --navy:#1d3c6e;
  --brand:#1a62b8;
  --sky:#2aa7e4;
  --hero-top:#1f8fe0;
  --hero-bottom:#0a5fc0;
  --yellow:#ffd21f;
  --orange:#f7a400;
  --green-top:#a6e23a;
  --green-bottom:#5fb30f;
  --page:#efefef;
  --card:#ffffff;
  --heading:#454545;
  --muted:#9a9a9a;
  --footer:#0b0b0b;
  --white:#ffffff;
}
*{margin:0;padding:0;box-sizing:border-box}
html,body{width:837px;height:1200px;overflow:hidden}
body{background:var(--page);font-family:"Open Sans",Arial,sans-serif;color:var(--heading)}
.page{position:relative;width:837px;height:1200px;overflow:hidden;
  background:repeating-linear-gradient(90deg,#f1f1f1 0 3px,#ebebeb 3px 4px)}
.abs{position:absolute}

/* header */
.site-header{left:0;top:0;width:837px;height:55px;background:var(--white);z-index:3}
.brand{left:72px;top:17px;display:flex;align-items:center;gap:6px;
  font-family:"Roboto Condensed",Arial,sans-serif;font-weight:700;font-size:21px;color:var(--brand)}
.brand-dot{width:12px;height:12px;border-radius:50%;background:var(--orange)}
.main-nav{left:323px;top:23px;display:flex;gap:0;list-style:none;
  font-family:"Roboto Condensed",Arial,sans-serif;font-weight:700;font-size:10.5px;color:var(--navy)}
.main-nav li{height:19px;line-height:19px;padding:0 7px;text-transform:uppercase}
.main-nav .is-active{background:var(--sky);color:var(--white);margin:0 2px}
.main-nav .login{background:var(--yellow);color:var(--white);margin-left:9px;padding:0 4px}

/* hero */
.hero{left:0;top:55px;width:837px;height:360px;
  background:radial-gradient(ellipse at 30% 10%,#35b2f5 0%,var(--hero-top) 40%,var(--hero-bottom) 100%)}
.hero-title{left:70px;top:115px;width:520px;color:var(--white);
  font-family:"Roboto Condensed",Arial,sans-serif;font-weight:400;font-size:25px;line-height:32px}
.btn{display:block;text-align:center;color:var(--white);text-transform:uppercase;
  font-family:"Roboto Condensed",Arial,sans-serif;font-weight:700;font-size:16px;
  box-shadow:0 4px 5px rgba(0,0,0,.25)}
.btn-buy{left:71px;top:198px;width:126px;height:32px;line-height:32px;
  background:linear-gradient(#ffe24a,var(--orange))}
.btn-trial{left:207px;top:198px;width:126px;height:32px;line-height:32px;
  background:linear-gradient(var(--green-top),var(--green-bottom))}
.search-field{left:70px;width:260px;height:32px;border-radius:16px;background:var(--white);
  box-shadow:0 2px 3px rgba(0,0,0,.2);padding-left:19px;line-height:32px;
  font-style:italic;font-size:12.5px;color:#b9b9b9}
.search-field svg{position:absolute;right:11px;top:6px}
.showcase{left:400px;top:140px;width:365px;height:365px;border-radius:10px 10px 40px 40px;
  background:linear-gradient(160deg,#2a2a2a 0%,#3c3c3c 12%,#7ccf5a 35%,#1f8f3a 60%,#d9d9d9 78%,#f2f2f2 100%);z-index:2}

/* contact strip */
.touch-label{left:72px;top:456px;font-family:"Roboto Condensed",Arial,sans-serif;
  font-weight:700;font-size:12px;color:var(--navy);text-transform:uppercase}
.social-tile{top:438px;width:42px;height:42px;border-radius:8px;box-shadow:0 2px 3px rgba(0,0,0,.3)}

/* feature cards */
.feature-card{top:532px;width:221px;height:181px;background:var(--card);box-shadow:0 1px 3px rgba(0,0,0,.15)}
.feature-icon{position:absolute;left:20px;top:-8px;width:58px;height:56px;border-radius:6px}
.feature-title{position:absolute;left:88px;top:20px;font-family:"Roboto Condensed",Arial,sans-serif;
  font-weight:300;font-size:26px;color:var(--heading)}
.feature-text{position:absolute;left:22px;top:68px;width:177px;text-align:center;
  font-style:italic;font-size:10.6px;line-height:17px;color:var(--muted)}
.btn-learn{position:absolute;left:48px;top:163px;width:126px;height:32px;line-height:32px;
  background:linear-gradient(#ffe24a,var(--orange))}

/* blog */
.blog-card{left:72px;top:759px;width:455px;height:238px;background:var(--card);box-shadow:0 1px 3px rgba(0,0,0,.15)}
.blog-icon{position:absolute;left:20px;top:-6px;width:62px;height:58px;border-radius:6px;
  background:linear-gradient(135deg,#f3e6cf,#d9a86a)}
.blog-title{position:absolute;left:99px;top:18px;font-family:"Roboto Condensed",Arial,sans-serif;
  font-weight:300;font-size:26px;color:var(--heading)}
.post{position:absolute;left:20px;width:415px}
.post-title{font-size:12px;color:#555;margin-bottom:6px}
.post-text{font-style:italic;font-size:10.4px;line-height:17px;color:var(--muted)}
.read-more{display:inline-block;background:var(--sky);color:var(--white);font-style:normal;
  font-size:6.5px;font-weight:700;text-transform:uppercase;padding:0 5px;line-height:13px;margin-left:6px}
.post-rule{position:absolute;left:20px;top:138px;width:410px;border-top:1px dashed #d8d8d8}

/* side */
.video{left:542px;top:759px;width:221px;height:147px;background:linear-gradient(135deg,#9fb0c0,#d6dde4 50%,#5b6b7c)}
.video-bar{position:absolute;left:0;bottom:0;width:100%;height:18px;background:rgba(0,0,0,.75)}
.video-track{position:absolute;left:38px;bottom:8px;width:130px;height:3px;background:#555}
.video-progress{position:absolute;left:0;top:0;width:55px;height:3px;background:var(--sky)}
.invite{left:542px;top:921px;width:221px;height:76px;background:linear-gradient(#3c92dd,#1663b8);color:var(--white);
  font-family:"Roboto Condensed",Arial,sans-serif;text-align:center}
.invite-line{position:absolute;left:40px;top:14px;width:170px;font-size:12.5px}
.invite-name{position:absolute;left:40px;top:32px;width:170px;font-size:24px;font-weight:700}

/* footer */
.site-footer{left:0;top:1032px;width:837px;height:168px;background:var(--footer);color:var(--white);
  font-family:"Roboto Condensed",Arial,sans-serif}
.footer-heading{position:absolute;top:13px;font-size:13.5px;font-weight:400}
.footer-links{position:absolute;top:40px;list-style:none;font-family:Arial,sans-serif;font-size:9.5px}
.footer-links li{height:22.5px;padding-left:17px;position:relative}
.footer-links li::before{content:"";position:absolute;left:0;top:2px;border-left:6px solid var(--white);
  border-top:4px solid transparent;border-bottom:4px solid transparent}
.social-links{position:absolute;left:648px;top:37px;list-style:none;font-family:Arial,sans-serif;font-size:9.5px}
.social-links li{display:flex;align-items:center;gap:10px;height:28px}
.social-ring{width:18px;height:18px;border:1.5px solid var(--white);border-radius:50%}
.footer-rule{position:absolute;left:72px;top:132px;width:692px;border-top:1px solid #222}
.copyright{position:absolute;left:72px;top:143px;font-family:Arial,sans-serif;font-size:9.5px}
</style>
</head>
<body>
<div class="page">

  <header class="site-header abs">
    <div class="brand abs"><span class="brand-dot"></span>RankLift.net</div>
    <ul class="main-nav abs">
      <li>About Us</li><li>Services</li><li class="is-active">Features</li><li>Resources</li>
      <li>Free Trial</li><li>FAQ</li><li>Contact</li><li class="login">Log In</li>
    </ul>
  </header>

  <section class="hero abs"></section>
  <h1 class="hero-title abs">Boost Your Search Engine Rankings Using Legal Back Linking Techniques</h1>
  <a class="btn btn-buy abs">Buy Now</a>
  <a class="btn btn-trial abs">Free Trial</a>
  <div class="search-field abs" style="top:256px">Enter Your URL
    <svg width="22" height="22" viewBox="0 0 22 22"><circle cx="8" cy="8" r="6" fill="none" stroke="#aaa" stroke-width="2"/><line x1="12.5" y1="12.5" x2="20" y2="20" stroke="#aaa" stroke-width="3" stroke-linecap="round"/></svg></div>
  <div class="search-field abs" style="top:298px">Enter Your Keywords Here
    <svg width="22" height="22" viewBox="0 0 22 22"><circle cx="8" cy="8" r="6" fill="none" stroke="#aaa" stroke-width="2"/><line x1="12.5" y1="12.5" x2="20" y2="20" stroke="#aaa" stroke-width="3" stroke-linecap="round"/></svg></div>
  <div class="search-field abs" style="top:338px">Type In Competitor URL Here
    <svg width="22" height="22" viewBox="0 0 22 22"><circle cx="8" cy="8" r="6" fill="none" stroke="#aaa" stroke-width="2"/><line x1="12.5" y1="12.5" x2="20" y2="20" stroke="#aaa" stroke-width="3" stroke-linecap="round"/></svg></div>
  <div class="showcase abs" role="img" aria-label="Desktop monitor showing rising green growth chart and arrow"></div>

  <p class="touch-label abs">Get In Touch With Us</p>
  <span class="social-tile abs" style="left:212px;background:#3a62b5"></span>
  <span class="social-tile abs" style="left:262px;background:#38b2e8"></span>
  <span class="social-tile abs" style="left:314px;background:#f8a51c"></span>

  <article class="feature-card abs" style="left:72px">
    <div class="feature-icon" role="img" aria-label="Colourful bar chart icon" style="background:linear-gradient(90deg,#5cb82a,#f4c21b,#f07a1a)"></div>
    <h2 class="feature-title">SEO Basics</h2>
    <p class="feature-text">Vestibulum feugiat magna in mi tincid-unt a blandit dui mollis. Curabitur euis-mod justo vitae massa sagittis dictum. Quisque ut nulla leo.</p>
    <a class="btn btn-learn">Learn More</a>
  </article>
  <article class="feature-card abs" style="left:306px">
    <div class="feature-icon" role="img" aria-label="Magnifying glass icon" style="background:linear-gradient(135deg,#e4eef5,#9aa6b0)"></div>
    <h2 class="feature-title" style="left:72px">Expect</h2>
    <p class="feature-text">Vestibulum feugiat magna in mi tincid-unt a blandit dui mollis. Curabitur euis-mod justo vitae massa sagittis dictum. Quisque ut nulla leo.</p>
    <a class="btn btn-learn">Learn More</a>
  </article>
  <article class="feature-card abs" style="left:542px">
    <div class="feature-icon" role="img" aria-label="Cardboard box with globe icon" style="background:linear-gradient(135deg,#e2c07f,#b7843f)"></div>
    <h2 class="feature-title">White Label</h2>
    <p class="feature-text">Vestibulum feugiat magna in mi tincid-unt a blandit dui mollis. Curabitur euis-mod justo vitae massa sagittis dictum. Quisque ut nulla leo.</p>
    <a class="btn btn-learn">Learn More</a>
  </article>

  <section class="blog-card abs">
    <div class="blog-icon" role="img" aria-label="Notebook and pencil icon"></div>
    <h2 class="blog-title">Latest Blog Posts</h2>
    <div class="post" style="top:68px">
      <h3 class="post-title">Native Advertising</h3>
      <p class="post-text">Vestibulum feugiat magna in mi tincidunt a blandit dui mollis. Curabitur euismod justo vitae massa sagittis dictum. Quisque ut nulla leo. <span class="read-more">Read More</span></p>
    </div>
    <div class="post-rule"></div>
    <div class="post" style="top:153px">
      <h3 class="post-title">Teething Pains</h3>
      <p class="post-text">Vestibulum feugiat magna in mi tincidunt a blandit dui mollis. Curabitur euismod justo vitae massa sagittis dictum. Quisque ut nulla leo. <span class="read-more">Read More</span></p>
    </div>
  </section>

  <div class="video abs" role="img" aria-label="Video still of a business team in an office">
    <svg class="abs" style="left:87px;top:44px" width="48" height="48" viewBox="0 0 48 48"><circle cx="24" cy="24" r="23" fill="rgba(255,255,255,.85)"/><path d="M19 14 L35 24 L19 34 Z" fill="#8a8a8a"/></svg>
    <div class="video-bar"><div class="video-track"><div class="video-progress"></div></div></div>
  </div>
  <div class="invite abs">
    <p class="invite-line">Invite Your Friends via</p>
    <p class="invite-name">FRIENDSPACE</p>
  </div>

  <footer class="site-footer abs">
    <h4 class="footer-heading" style="left:72px">Company</h4>
    <ul class="footer-links" style="left:72px"><li>About Us</li><li>Why RankLift</li><li>FAQ</li><li>Affiliate Program</li></ul>
    <ul class="footer-links" style="left:215px"><li>Tips To Using Our System</li><li>Contact us</li><li>Terms of Use</li><li>Privacy Policy</li></ul>
    <h4 class="footer-heading" style="left:370px">Services</h4>
    <ul class="footer-links" style="left:371px"><li>Link Building</li><li>Local SEO</li><li>Free Trial</li><li>Free Keyword Analysis Tools</li></ul>
    <h4 class="footer-heading" style="left:534px">SEO</h4>
    <ul class="footer-links" style="left:533px"><li>SEO Basics</li><li>SEO Tips</li><li>On Page SEO</li><li>Off Page SEO</li></ul>
    <h4 class="footer-heading" style="left:646px">Get in Touch</h4>
    <ul class="social-links"><li><span class="social-ring"></span>Friendspace</li><li><span class="social-ring"></span>Chirper</li></ul>
    <div class="footer-rule"></div>
    <p class="copyright">RankLift 2013 Copyright! All rights Reserved!</p>
  </footer>

</div>
</body>
</html>
```